Business Cards Design for the electrical wholesaler: clean bold dynamic :)

We need a business card design that would follow our latest brand guidelines. As an electrical wholesaler we want to bring a fresh look and feel into the industry. The design should be clean bold and dynamic. It should come alive with the renewed energy of our green colour. Our grey colour should keep things balanced and complement the notion of maturity and responsibility. We employ Lato as a corporate font however are not bound by this font and we’re open to interpretation here.

Target Market(s)

Electrical contractors

Industry/Entity Type

Business

Contact Information for Business Card

Logo
Name & Surname: Olena Dovbush
Job Title: Director of Marketing
Email: helen.dovbush@mailvane.example
Cell phone: XXX.XXX.XXXX
Address: 20917 - 87 Ave. Edmonton, AB, Canada. T6K 2R8
Business Phone: 780.555.0187
Website: www.qorvil.example

Font styles to use
Other font styles liked:
• Lato

Requirements
Must have
• Logo & website
Nice to have
• Brand elements - some of them you may find in the attached Brand Guidelines (e.g. three lines on the background signifying "W")

```html
<!DOCTYPE html>
<html lang="en">
<head>
<meta charset="utf-8">
<title>Qorvil Business Cards</title>
<link href="https://fonts.googleapis.com/css2?family=Lato:wght@400;700&display=swap" rel="stylesheet">
<style>
  :root {
    --green: #8dc63f;
    --charcoal: #555759;
    --text-grey: #58595b;
    --mist: #d6dde2;
    --paper: #ffffff;
    --backdrop: #ffffff;
    --card-shadow: rgba(0, 0, 0, 0.28);
  }
  * { margin: 0; padding: 0; box-sizing: border-box; }
  html, body {
    width: 1200px; height: 1000px; overflow: hidden;
    background: var(--backdrop);
    font-family: "Lato", sans-serif;
  }
  .canvas { position: relative; width: 1200px; height: 1000px; }
  .card {
    position: absolute; width: 736px; height: 420px; overflow: hidden;
    box-shadow: 3px 5px 8px var(--card-shadow);
  }
  .card svg.shapes { position: absolute; inset: 0; }
  .card-back { left: 358px; top: 473px; background: var(--charcoal); }
  .card-front {
    left: 73px; top: 97px; background: var(--paper);
    outline: 1px solid rgba(0, 0, 0, 0.06);
  }

  .wordmark {
    position: absolute; display: flex; align-items: center; gap: 12px;
    font-weight: 700; line-height: 1;
  }
  .wordmark .mark-square { display: block; background: var(--green); }
  .front-wordmark { right: 70px; top: 58px; font-size: 62px; color: var(--charcoal); }
  .front-wordmark .mark-square { width: 40px; height: 40px; }

  .back-lockup {
    position: absolute; left: 246px; top: 200px; width: 240px;
    display: flex; flex-direction: column; align-items: center;
  }
  .back-lockup .wordmark { position: static; font-size: 84px; color: var(--paper); }
  .back-lockup .mark-square { width: 52px; height: 52px; }
  .tagline {
    margin-top: 16px; font-size: 13px; font-weight: 700; letter-spacing: 1.6px;
    color: var(--paper); white-space: nowrap;
  }

  .person { position: absolute; left: 90px; top: 204px; color: var(--text-grey); }
  .person .name { font-size: 28px; font-weight: 700; color: var(--green); line-height: 1; margin-bottom: 12px; }
  .contact-line { font-size: 19px; line-height: 35px; white-space: nowrap; }
  .contact-line.email { font-size: 16px; }
  .label { font-weight: 700; display: inline-block; width: 24px; }

  .company { position: absolute; left: 370px; top: 206px; color: var(--text-grey); }
  .company .web { font-weight: 700; }
</style>
</head>
<body>
<div class="canvas">

  <section class="card card-back" aria-label="Card back">
    <svg class="shapes" width="736" height="420" viewBox="0 0 736 420">
      <polygon points="690,0 736,0 736,134" fill="var(--green)"/>
      <polygon points="0,167 89,420 0,420" fill="var(--mist)"/>
    </svg>
    <div class="back-lockup">
      <div class="wordmark"><span class="mark-square"></span>qorvil</div>
      <div class="tagline">ELECTRICAL WHOLESALERS</div>
    </div>
  </section>

  <section class="card card-front" aria-label="Card front">
    <svg class="shapes" width="736" height="420" viewBox="0 0 736 420">
      <polygon points="689,0 736,0 736,133" fill="var(--green)"/>
      <polygon points="0,165 89,420 0,420" fill="var(--mist)"/>
    </svg>
    <div class="wordmark front-wordmark"><span class="mark-square"></span>qorvil</div>

    <div class="person">
      <p class="name">Olena Dovbush</p>
      <p class="contact-line">Director of Marketing</p>
      <p class="contact-line email">helen.dovbush@mailvane.example</p>
      <p class="contact-line"><span class="label">m</span>780.555.0187</p>
    </div>

    <div class="company">
      <p class="contact-line">20917 - 87 Ave. Edmonton, AB,</p>
      <p class="contact-line">Canada. T6K 2R8</p>
      <p class="contact-line"><span class="label">t</span>780.555.0187</p>
      <p class="contact-line"><span class="label">f</span>780.555.0187</p>
      <p class="contact-line web">www.qorvil.example</p>
    </div>
  </section>

</div>
</body>
</html>
```